OPF - Brochure 52 week Curriculum

Oak Path Fellows, Inc. wants to create a distribution Brochure. In the Bible (Matthew 28:18-20)- JESUS said to "TEACH" others what HE has commanded. we want to "PUT IN PRINT"

these 52 lines summarize HIS teachings
we want to use as our Curriculum teaching men ...

incorporate our statements and two main passages of scripture
(see attach pictures of headquarter lobby) to brand uniformity and consistency... we have summarized into 52 groups, but its NOT required to have numbers...
Purpose = obey GOD
Mission = love others
Vision = Development God fearing men globally.

The designer can have freedom in layout and sizing.
we were thinking bi fold , but again... designer has freedom
Please incorporate our colors (white, black, gray) using color wheel provided and our LOGO with website.

```html
<!DOCTYPE html>
<html lang="en">
<head>
<meta charset="utf-8">
<title>OPF – 52 Summaries of Jesus' Teachings Brochure</title>
<link href="https://fonts.googleapis.com/css2?family=Noto+Serif:wght@400;700&family=Oswald:wght@400;500;600&family=Open+Sans:wght@800&display=swap" rel="stylesheet">
<style>
  :root{
    --backdrop:#7f7f7f;
    --page:#ebebeb;
    --page-shade:#e2e2e2;
    --ink:#161616;
    --black:#000;
    --black-soft:#060606;
    --quote-gray:#555;
    --white:#fff;
    --rule:#222;
  }
  *{margin:0;padding:0;box-sizing:border-box}
  html,body{width:840px;height:1200px;overflow:hidden;background:var(--backdrop)}
  .canvas{position:relative;width:840px;height:1200px}
  .spread{position:absolute;left:23px;width:794px;height:562px;box-shadow:0 2px 8px rgba(0,0,0,.45);overflow:hidden}
  .spread--outer{top:28px;background:var(--black)}
  .spread--inner{top:610px;background:var(--page)}

  /* body text */
  .col{position:absolute;font-family:"Noto Serif",serif;color:var(--ink);overflow:hidden}
  .col h2{font-family:"Noto Serif",serif;font-weight:700;font-size:9.6px;line-height:11.2px;text-transform:uppercase;margin:0 0 3px}
  .col h2 + ul{margin-top:0}
  .col ul{list-style:none}
  .col > ul > li{position:relative;padding-left:9px;font-weight:700;font-size:6.6px;line-height:8.4px;margin-bottom:6px;text-align:justify}
  .col > ul > li::before{content:"•";position:absolute;left:0}
  .col li ul{margin-top:1px}
  .col li ul li{position:relative;padding-left:9px;font-weight:400;text-align:justify}
  .col li ul li::before{content:"•";position:absolute;left:0}
  .col .gap{margin-top:4px}

  .footer{position:absolute;font-family:"Oswald",sans-serif;font-size:7.6px;color:var(--ink);border-top:0.8px solid var(--rule);padding-top:5px}

  /* outer spread */
  .back-page{position:absolute;left:0;top:0;width:203px;height:562px;background:var(--page)}
  .mid-panel{position:absolute;left:203px;top:0;width:194px;height:562px;background:var(--black)}
  .cover{position:absolute;left:397px;top:0;width:397px;height:562px;background:var(--black-soft)}
  .quote-mark{position:absolute;font-family:"Open Sans",sans-serif;font-weight:800;color:var(--quote-gray);font-size:190px;line-height:1}
  .quote-mark--open{left:262px;top:132px}
  .quote-mark--close{left:262px;top:294px}
  .statements{position:absolute;right:412px;top:202px;text-align:right;font-family:"Open Sans",sans-serif;font-weight:800;color:var(--white);font-size:17.5px;line-height:20px;text-transform:uppercase}
  .statements p{margin-bottom:6px}
  .statements p.vision{margin-top:2px}
  .brand{position:absolute;left:468px;top:55px;width:150px;text-align:center;color:var(--white);font-family:"Oswald",sans-serif}
  .brand-name{font-size:44px;font-weight:600;line-height:1;letter-spacing:1px}
  .brand-web{font-size:7px;font-weight:500;letter-spacing:.2px;margin-top:2px}
  .title{position:absolute;left:434px;top:148px;color:var(--white);font-family:"Oswald",sans-serif;font-weight:600;text-transform:uppercase}
  .title-num{position:absolute;left:0;top:0;font-size:78px;line-height:76px;letter-spacing:-3px}
  .title-lines{position:absolute;left:75px;top:4px;font-size:31px;line-height:34px;white-space:nowrap}
  .title-last{position:absolute;left:0;top:72px;font-size:32px;line-height:34px}
  .cover-art{position:absolute;left:434px;top:249px;width:383px;height:313px;background:linear-gradient(160deg,#9c9c9c 0%,#6a6a6a 30%,#2a2a2a 65%,#000 100%)}
</style>
</head>
<body>
<div class="canvas">

  <!-- Outer spread: back page, middle panel, front cover -->
  <section class="spread spread--outer">
    <div class="back-page"></div>
    <div class="mid-panel"></div>
    <div class="cover"></div>

    <div class="col" style="left:38px;top:31px;width:155px;height:490px;">
      <h2>Forgiveness (Jesus taught about the importance of both receiving and giving forgiveness)</h2>
      <ul>
        <li>Forgive others: Matthew<ul><li>6:12, 14, Mark 11:25-26, Luke 6:37</li></ul></li>
        <li>JESUS emphasized that forgiveness is linked to forgiving others<ul><li>(Matthew 6:14-15)</li></ul></li>
        <li>Forgiveness should be extended limitlessly to those who repent<ul><li>(Luke 17:3-4; Matthew 18:21-22).</li></ul></li>
        <li>forgiveness is also illustrated as the cancellation of debt<ul><li>(Matthew 18:21-35).</li></ul></li>
      </ul>
      <h2>Humility and Service</h2>
      <ul>
        <li>JESUS stated that humility leads to being honored<ul><li>(Luke 14:11; Matthew 23:12)</li></ul></li>
        <li>True greatness is found in serving others<ul><li>(Matthew 20:26-28).</li></ul></li>
        <li>The Bible also states that God opposes the proud but shows favor to the humble<ul><li>(James 4:6; 1 Peter 5:5).</li></ul></li>
      </ul>
      <h2>Warning Against Self-Righteousness and Judgment</h2>
      <ul>
        <li>Jesus warned against hypocrisy, particularly the hypocrisy of the Pharisees<ul><li>(Luke 12:1).</li></ul></li>
      </ul>
      <h2>Money (Jesus taught about using money and possessions responsibly.)</h2>
      <ul>
        <li>JESUS advised storing up treasures in Heaven rather than on Earth<ul><li>(Matthew 6:19-21)</li></ul></li>
        <li>JESUS stated that it is impossible to serve both God and money<ul><li>(Matthew 6:24).</li></ul></li>
      </ul>
    </div>
    <div class="footer" style="left:38px;top:523px;width:165px;">52 Summaries of Jesus' Teaching</div>

    <div class="quote-mark quote-mark--open">“</div>
    <div class="quote-mark quote-mark--close">”</div>
    <div class="statements">
      <p>Obey God</p>
      <p>Love Others</p>
      <p class="vision">Development<br>God Fearing<br>Men Globally</p>
    </div>

    <div class="brand">
      <div class="brand-name">OPF</div>
      <div class="brand-web">WWW.OAKPATHFELLOWS.COM</div>
    </div>
    <h1 class="title">
      <span class="title-num">52</span>
      <span class="title-lines">Summaries<br>of Jesus’</span>
      <span class="title-last">Teachings</span>
    </h1>
    <div class="cover-art" role="img" aria-label="Illustration of a man walking across large perspective lettering reading 52 Summaries of Jesus' Teachings, fading into black"></div>
  </section>

  <!-- Inner spread -->
  <section class="spread spread--inner">
    <div style="position:absolute;left:397px;top:0;width:397px;height:562px;background:linear-gradient(90deg,var(--page-shade),var(--page) 20%);"></div>

    <div class="col" style="left:38px;top:30px;width:156px;height:490px;">
      <h2>Regarding God and Righteousness</h2>
      <ul>
        <li>Repent: Change your mind and actions towards sin, as the Kingdom of Heaven is near. Turn away from sin and toward GOD.<ul><li>Matthew 4:17, Luke 13:3. Repent: This is the call to turn away from sin and embrace the good news of salvation through Jesus Christ. Found in Mark 1:15.</li></ul></li>
        <li>Accept the Good News of salvation offered through Jesus.</li>
        <li>Believe in the Son of God, Jesus Christ: This is essential for salvation and receiving the Holy Spirit.<ul><li>John 6:29, John 14:11</li></ul></li>
        <li>Have faith in God, and trust in Jesus as the Son of God.</li>
        <li>Be born again:<ul><li>John 3:7 Be born again (of water and the Spirit): Experience a spiritual transformation necessary for entrance into God’s Kingdom.</li></ul></li>
        <li>Give your utmost devotion and affection to God. Love God with all your heart, soul, mind, and strength:<ul><li>Matthew 22:37-38, Mark 12:30, Luke 10:27</li></ul></li>
        <li>Honor God’s Law: Understand that Jesus did not come to abolish the Law but to fulfill it and to magnify its application in the heart.</li>
      </ul>
      <h2>Regarding Relationships and Ethics</h2>
      <ul>
        <li>Love your Neighbor as yourself:<ul><li>Matthew 22:39, Mark 12:31, Luke 10:27, Leviticus 19:18. Love one another, as I have loved you: Show sacrificial love to fellow believers.</li></ul></li>
        <li>The Golden Rule: Treat others as you would want to be treated.<ul><li>(Matthew 7:12). This encapsulates how to treat everyone with respect, kindness, and understanding.</li></ul></li>
        <li>Be reconciled to your brother: Seek peace</li>
      </ul>
    </div>

    <div class="col" style="left:203px;top:30px;width:156px;height:490px;">
      <ul>
        <li style="padding-left:9px;">and forgiveness when relationships are broken.</li>
        <li>Go to those who offend you: Address offenses directly and privately before involving others.</li>
        <li>Forgive offenders: Extend forgiveness to those who hurt you and forgive often. Forgive others: This is essential for receiving God’s forgiveness.</li>
        <li>Love your enemies and pray for those who persecute you<ul><li>Matthew 5:44, Luke 6:27- Extend compassion even to those who mistreat you.</li></ul></li>
      </ul>
      <h2>Regarding Personal Conduct and Attitudes</h2>
      <ul>
        <li>Be baptized: Be immersed in water as a symbol of your new life in Christ.</li>
        <li>Take, eat, and drink in remembrance of Me (Communion/Lord’s Supper): Participate in the commemoration of Jesus’ sacrifice.</li>
        <li>Let your light shine before others:<ul><li>Matthew 5:16. Followers are called to live in such a way that their good deeds bring glory to GOD. Demonstrate good works to the world.</li></ul></li>
        <li>Care for the less fortunate: Help those in need, such as the hungry, thirsty, strangers, naked, sick, and imprisoned,<ul><li>according to Luke 14:13-14, Matthew 25:31-46.</li></ul></li>
        <li>Deny yourself, Take up your cross daily and follow Jesus: This signifies a commitment to discipleship, even in the face of hardship.<ul><li>this teaching is found in Luke 9:23-24; Matthew 16:24-25. Prioritize following Jesus above your own desires and be willing to endure hardship for His sake.</li></ul></li>
        <li>Fast: Engage in fasting, but do so for the right reasons and not for outward show.</li>
        <li>Be wise as serpents and innocent as doves:<ul><li>Matthew 10:16</li></ul></li>
        <li>Do not worry about your life or material possessions: Trust God to provide for your</li>
      </ul>
    </div>
    <div class="footer" style="left:38px;top:523px;width:321px;">52 Summaries of Jesus' Teaching</div>

    <div class="col" style="left:434px;top:30px;width:156px;height:490px;">
      <ul>
        <li>needs. Trust God to provide for your needs.<ul><li>Matthew 6:34</li></ul></li>
        <li>Lay up treasures in heaven: Focus on building a spiritual inheritance rather than accumulating earthly wealth.<ul><li>Matthew 6:19-21</li></ul></li>
        <li>Be a servant: Seek greatness through humble service to others. Serve one another:<ul><li>Matthew 20:25-28</li></ul></li>
      </ul>
      <h2>Prayer</h2>
      <ul>
        <li>Jesus provided guidance on prayer, teaching that it should be done in private and with sincerity<ul><li>(Matthew 6:5-8).</li></ul></li>
        <li>He also linked prayer to having a forgiving heart<ul><li>(Mark 11:25; Matthew 18:18-20).</li></ul></li>
        <li>HE encouraged praying with simple faith and persistence<ul><li>(Luke 11:5-13; Matthew 21:21-22).</li></ul></li>
        <li>Pray: Engage in prayer consistently, with sincerity and according to Jesus’ example.</li>
        <li>Prayer for our enemies:<ul><li>Luke 23:24, Matthew 5:44</li></ul></li>
        <li>Pray for others : intercession</li>
        <li>Pray for laborers: Seek God to send workers into the harvest field of souls. Pray for kingdom laborers:<ul><li>Matthew 9:38, Luke 10:2</li></ul></li>
      </ul>
      <h2>Regarding Outreach and Discipleship</h2>
      <ul>
        <li>Go and make disciples of all nations: Evangelize and teach others to follow Jesus’ commands: This is a central command, emphasizing the importance of evangelism and discipleship.<ul><li>Matthew 28:18-20. Teach others to obey all that Jesus commanded: Passing on the teachings of Christ to new believers is a key aspect of discipleship.</li></ul></li>
        <li>Feed My Sheep: Care for and nourish the</li>
      </ul>
    </div>

    <div class="col" style="left:600px;top:30px;width:156px;height:490px;">
      <ul>
        <li>spiritual lives of believers.</li>
        <li>Receive God’s power: Be filled with the Holy Spirit to effectively carry out God’s work.</li>
      </ul>
      <h2>Cautions and Warnings</h2>
      <ul>
        <li>Beware of false prophets: Be discerning and recognize those who may mislead others with false teachings.</li>
        <li>Beware of leaven (doctrine) of the Pharisees and Sadducees: Avoid hypocrisy and legalism.</li>
        <li>Be alert and reliant on God’s strength to overcome temptation.</li>
        <li>Do not cast pearls before swine: Use discretion and avoid sharing sacred things with those who may devalue or disrespect them.</li>
      </ul>
      <h2>Living as a Disciple</h2>
      <ul>
        <li>Be merciful: Show compassion to others, just as God is merciful. Act with kindness and compassion towards others.<ul><li>Luke 6:36</li></ul></li>
        <li>Care for those in distress: Help the hungry, thirsty, strangers, naked, sick, and imprisoned.</li>
        <li>Recognize your own imperfections and avoid judging others harshly.<ul><li>Matthew 7:1-2, Luke 6:37.</li></ul></li>
        <li>Focus on examining your own faults before criticizing others. He taught against judging others, stating that the standard by which you judge will be applied to you<ul><li>(Matthew 7:1-2).</li></ul></li>
        <li>40. Seek God’s kingdom first: Make God and his righteousness your highest priority. Prioritize God’s reign and right way of living above all else.<ul><li>Found in Matthew 6:33.</li></ul></li>
        <li>Abide in JESUS:<ul><li>John 15:4, John 6:35, 40, 47, John 14:27.</li></ul></li>
        <li>Follow JESUS:<ul><li>Matthew 4:19, Luke 5:28</li></ul></li>
      </ul>
    </div>
    <div class="footer" style="left:434px;top:523px;width:322px;text-align:right;">52 Summaries of Jesus' Teaching</div>
  </section>

</div>
</body>
</html>
```